Mission statement design for a secondary school

We have the content of our mission statement and need an appealing layout. The design should fit on a poster or A4 page. The content grouping in the document should also be graphically recognizable. Our target group are young people and their parents as well as the school staff, which is why we need a modern design that is not out after 2 years. It must be easy to grasp visually and graphically simple.

Target Market(s)

Actors of the school

Requirements
Must have
• cantonal logo including school name see document can be integrated as a header
Should not have
• References to trademarks or third parties

```html
<!DOCTYPE html>
<html lang="de">
<head>
<meta charset="utf-8">
<title>Unser Leitbild – Sekundarschule Lindenfeld</title>
<link rel="stylesheet" href="https://fonts.googleapis.com/css2?family=Poppins:wght@400;600;700;800&display=swap">
<style>
  :root{
    --bg:#d9d9d9;
    --paper:#ffffff;
    --band:#6e6e6e;
    --footer:#5b5b5b;
    --red:#ee6f6d;
    --red-light:#f28380;
    --red-dark:#e84d4b;
    --ink:#555555;
    --text:#6a6a6a;
    --rule:#d8d8d8;
    --white:#ffffff;
  }
  *{box-sizing:border-box;margin:0;padding:0}
  html,body{width:1200px;height:1200px;overflow:hidden;background:var(--bg);font-family:"Poppins",sans-serif}
  .stage{position:relative;width:1200px;height:1200px}
  .flyer{
    position:absolute;left:197px;top:30px;width:1012px;height:1432px;
    transform:scale(0.7961);transform-origin:0 0;
    background:var(--paper);overflow:hidden;
  }
  .header-band{position:absolute;left:0;top:0;width:1012px;height:158px;background:var(--band)}
  .ribbon{position:absolute;left:37px;top:0;width:190px;height:985px;filter:drop-shadow(10px 0 14px rgba(0,0,0,.18))}
  .ribbon-title{
    position:absolute;left:132px;top:452px;transform:translate(-50%,-50%) rotate(-90deg);
    white-space:nowrap;color:var(--white);font-weight:800;font-size:108px;letter-spacing:1px;line-height:1;
  }
  .headline{position:absolute;left:280px;top:28px;font-weight:700;font-size:40px;line-height:40px;color:var(--white)}
  .headline .accent{color:var(--red-light)}
  .categories{position:absolute;left:280px;top:116px;display:flex;gap:22px;color:var(--white);font-size:22px;line-height:30px}
  .categories span,.attitude li{display:flex;align-items:flex-start;gap:8px}
  .tick{flex:none;width:20px;height:20px;margin-top:5px}
  .tick path{fill:none;stroke:var(--red-light);stroke-width:2.6;stroke-linecap:round;stroke-linejoin:round}
  .attitude-title{position:absolute;left:280px;top:180px;font-weight:800;font-size:26px;line-height:28px;color:var(--ink)}
  .attitude-title .accent{color:var(--red)}
  .attitude{position:absolute;top:244px;list-style:none;font-size:17px;line-height:22px;color:var(--text)}
  .attitude li{margin-bottom:4px}
  .attitude .tick{width:18px;height:18px;margin-top:2px}
  .attitude.left{left:280px;width:360px}
  .attitude.right{left:668px;width:320px}
  .rule{position:absolute;height:0;border-top:2px dashed var(--rule)}
  .timeline{position:absolute;left:0;top:0;width:1012px;height:1432px;pointer-events:none}
  .section{position:absolute;left:402px;width:560px}
  .section.narrow{width:495px}
  .section h2{font-weight:700;font-size:26px;line-height:30px;color:var(--red);margin-bottom:10px}
  .section ul{list-style:none;font-size:17px;line-height:22px;color:var(--text)}
  .section li{margin-bottom:8px}
  .photo{position:absolute;left:0;top:940px;width:340px;height:492px}
  .footer-band{position:absolute;left:330px;top:1282px;width:682px;height:150px;background:var(--footer)}
  .contact{position:absolute;left:368px;top:1298px;color:var(--white);font-size:17px;line-height:21.5px;font-style:normal}
  .contact .school{font-weight:700}
  .contact .details{margin-top:2px;padding-left:12px;border-left:4px solid var(--red)}
  .contact strong{font-weight:700}
  .canton{position:absolute;left:677px;top:1305px;width:335px;height:127px}
  .canton-name{position:absolute;right:42px;top:1340px;text-align:right;color:var(--white);font-weight:600;font-size:29px;line-height:30px;letter-spacing:2px}
</style>
</head>
<body>
<div class="stage">
  <article class="flyer">
    <div class="header-band"></div>

    <svg class="ribbon" viewBox="0 0 190 985" aria-hidden="true">
      <defs>
        <linearGradient id="ribbonFill" x1="0" y1="0" x2="0" y2="1">
          <stop offset="0" stop-color="#f28380"/>
          <stop offset="1" stop-color="#e84d4b"/>
        </linearGradient>
      </defs>
      <polygon points="0,0 190,0 190,985 95,918 0,985" fill="url(#ribbonFill)"/>
    </svg>
    <div class="ribbon-title">UNSER LEITBILD</div>

    <h1 class="headline">ES GIBT DREI KATEGORIEN UND<br><span class="accent">DIE HALTUNG DER SCHULE.</span></h1>
    <div class="categories">
      <span><svg class="tick" viewBox="0 0 20 20"><path d="M3 10l5 5 9-10"/></svg>LERNEN</span>
      <span><svg class="tick" viewBox="0 0 20 20"><path d="M3 10l5 5 9-10"/></svg>ENTWICKLUNG</span>
      <span><svg class="tick" viewBox="0 0 20 20"><path d="M3 10l5 5 9-10"/></svg>GEMEINSCHAFT</span>
    </div>

    <h2 class="attitude-title"><span class="accent">HALTUNG</span><br>AN UNSERER SCHULE...</h2>
    <ul class="attitude left">
      <li><svg class="tick" viewBox="0 0 20 20"><path d="M3 10l5 5 9-10"/></svg><span>stehen die Lernenden im Mittelpunkt.</span></li>
      <li><svg class="tick" viewBox="0 0 20 20"><path d="M3 10l5 5 9-10"/></svg><span>begegnen wir uns respektvoll und wertschätzend.</span></li>
    </ul>
    <ul class="attitude right">
      <li><svg class="tick" viewBox="0 0 20 20"><path d="M3 10l5 5 9-10"/></svg><span>ist Integration selbstverständlich.</span></li>
      <li><svg class="tick" viewBox="0 0 20 20"><path d="M3 10l5 5 9-10"/></svg><span>setzen wir uns für lebenslanges Lernen ein.</span></li>
    </ul>
    <div class="rule" style="left:280px;top:333px;width:706px"></div>

    <svg class="photo" viewBox="0 0 340 492" role="img" aria-label="Foto: zwei lächelnde Jugendliche mit Schulordnern">
      <defs>
        <linearGradient id="photoFill" x1="0" y1="0" x2="0.4" y2="1">
          <stop offset="0" stop-color="#c7a58f"/>
          <stop offset="0.4" stop-color="#7d9f6a"/>
          <stop offset="0.75" stop-color="#2f7bc2"/>
          <stop offset="1" stop-color="#e3df2a"/>
        </linearGradient>
      </defs>
      <path d="M0,70 Q20,40 70,50 L130,10 Q220,-10 245,60 L255,150 Q325,170 340,260 L340,492 L0,492 Z" fill="url(#photoFill)"/>
    </svg>

    <svg class="timeline" viewBox="0 0 1012 1432" aria-hidden="true">
      <g fill="none" stroke-width="4">
        <line x1="330" y1="452" x2="330" y2="960" stroke="#ee6f6d" stroke-width="3"/>
        <circle cx="330" cy="405" r="46" fill="#fff" stroke="none"/>
        <path d="M330 359 A46 46 0 0 1 330 451" stroke="#6a6a6a"/>
        <path d="M330 451 A46 46 0 0 1 330 359" stroke="#ee6f6d"/>
        <g stroke="#6a6a6a" stroke-width="2" stroke-linejoin="round">
          <path d="M305 392 v24 q12 -4 25 4 q13 -8 25 -4 v-24 q-12 -4 -25 4 q-13 -8 -25 -4z"/>
          <line x1="330" y1="396" x2="330" y2="420"/>
          <path d="M320 386 q0 -12 10 -12 q10 0 10 12"/>
        </g>
        <circle cx="330" cy="732" r="46" fill="#fff" stroke="none"/>
        <path d="M330 686 A46 46 0 0 1 330 778" stroke="#6a6a6a"/>
        <path d="M330 778 A46 46 0 0 1 330 686" stroke="#ee6f6d"/>
        <g stroke="#6a6a6a" stroke-width="2" stroke-linecap="round">
          <path d="M322 744 q-10 -8 -10 -19 a18 18 0 0 1 36 0 q0 11 -10 19 v6 h-16z"/>
          <line x1="323" y1="755" x2="337" y2="755"/>
          <line x1="325" y1="760" x2="335" y2="760"/>
          <line x1="303" y1="725" x2="297" y2="725"/><line x1="357" y1="725" x2="363" y2="725"/>
          <line x1="308" y1="708" x2="303" y2="704"/><line x1="352" y1="708" x2="357" y2="704"/>
        </g>
        <circle cx="330" cy="1007" r="46" fill="#fff" stroke="none"/>
        <path d="M330 961 A46 46 0 0 1 330 1053" stroke="#6a6a6a"/>
        <path d="M330 1053 A46 46 0 0 1 330 961" stroke="#ee6f6d"/>
        <g stroke="#6a6a6a" stroke-width="2">
          <circle cx="322" cy="991" r="4"/><circle cx="338" cy="991" r="4"/>
          <circle cx="314" cy="1003" r="4"/><circle cx="330" cy="1003" r="4"/><circle cx="346" cy="1003" r="4"/>
          <path d="M305 1026 v-8 q0 -6 9 -6 q9 0 9 6 M321 1018 q0 -6 9 -6 q9 0 9 6 M337 1018 q0 -6 9 -6 q9 0 9 6 v8"/>
          <line x1="302" y1="1026" x2="358" y2="1026"/>
        </g>
      </g>
    </svg>

    <section class="section" style="top:352px">
      <h2>LERNEN</h2>
      <ul>
        <li>Wir begleiten unsere Lernenden hin zur Selbständigkeit.</li>
        <li>Wir unterstützen unsere Lernenden in ihrem individuellen Kompetenzerwerb.</li>
        <li>Wir ermöglichen allen Lernenden Erfolge.</li>
        <li>Die Unterrichtsinhalte orientieren sich an aktuellen Themen.</li>
        <li>Wir beurteilen transparent.</li>
        <li>Wir begegnen Heterogenität mit multiprofessionellen Teams.</li>
        <li>Wir schaffen eine wertschätzende und förderliche Atmosphäre.</li>
        <li>Unsere Schule bietet eine zeitgemässe Infrastruktur.</li>
      </ul>
    </section>
    <div class="rule" style="left:402px;top:667px;width:584px"></div>

    <section class="section" style="top:679px">
      <h2>ENTWICKLUNG</h2>
      <ul>
        <li>Wir entwickeln unsere Schule gemeinsam.</li>
        <li>Wir setzen unsere Fähigkeiten und Kräfte gezielt ein.</li>
        <li>Alle tragen Verantwortung.</li>
        <li>Wir lernen alle voneinander.</li>
        <li>Wir bilden uns kontinuierlich weiter.</li>
        <li>Wir reflektieren unser Handeln.</li>
        <li>Wir sind innovativ und gehen mutig unseren Weg.</li>
      </ul>
    </section>
    <div class="rule" style="left:402px;top:943px;width:584px"></div>

    <section class="section narrow" style="top:954px">
      <h2>GEMEINSCHAFT</h2>
      <ul>
        <li>Unsere Schule achtet die Gesundheit aller.</li>
        <li>Wir legen Wert auf eine offene Kommunikation.</li>
        <li>Unsere pädagogische Zusammenarbeit basiert auf einer professionellen Haltung.</li>
        <li>Die Eltern sind ein Teil unserer Schulgemeinschaft und<br>tragen Verantwortung.</li>
        <li>Wir haben an unserer Schule Freiräume innerhalb klarer Rahmenbedingungen.</li>
      </ul>
    </section>

    <div class="footer-band"></div>

    <address class="contact">
      <div class="school">sekundarschule lindenfeld</div>
      <div class="details">
        ahornweg 12<br>
        4100 lindenfeld<br>
        <strong>061 000 12 34</strong><br>
        <strong>info</strong>@sek-lindenfeld.ch
      </div>
    </address>

    <svg class="canton" viewBox="0 0 335 127" aria-hidden="true">
      <defs>
        <linearGradient id="cantonFill" x1="0" y1="0" x2="1" y2="0">
          <stop offset="0" stop-color="#f07572"/>
          <stop offset="1" stop-color="#e84d4b"/>
        </linearGradient>
      </defs>
      <polygon points="58,0 335,0 335,127 0,127" fill="url(#cantonFill)"/>
    </svg>
    <div class="canton-name">KANTON<br>NORDTAL</div>
  </article>
</div>
</body>
</html>
```